Book Cover Quieting Gnats, Shouldn'ts and Maybes, Climbing out of the valley of sorrow

Need a book cover design for my new web site..Drpeterwalsby.com (website under construction) I'm appearing on Echo of Meridia radio show and want to add a cover design of my book.

My book with enpower people to break the chain of limiting beliefs and unlock their true potential so they will finally experience the life of their dreams

Radio

```html
<!DOCTYPE html>
<html lang="en">
<head>
<meta charset="utf-8">
<title>Quieting Gnats, Shouldn'ts and Maybes — Book Cover</title>
<link rel="stylesheet" href="https://fonts.googleapis.com/css2?family=Archivo+Black&family=Open+Sans:wght@800&display=swap">
<style>
  :root {
    --paper: #ffffff;
    --frame-red: #b3151b;
    --title-ink: #0a0a0a;
    --subtitle-red: #c0141b;
    --author-green: #17861f;
    --skin: #f0c9a8;
    --tunic: #b08a2e;
  }
  html, body {
    margin: 0;
    padding: 0;
    width: 802px;
    height: 1200px;
    overflow: hidden;
    background: var(--paper);
  }
  .cover {
    position: relative;
    width: 802px;
    height: 1200px;
    background: var(--paper);
  }
  .cover-frame {
    position: absolute;
    left: 73px;
    top: 118px;
    width: 689px;
    height: 1012px;
    box-sizing: border-box;
    border: 3px solid var(--frame-red);
  }
  .hero-illustration {
    position: absolute;
    left: 134px;
    top: 212px;
    width: 256px;
    height: 330px;
    border-radius: 10px;
    background: linear-gradient(180deg, var(--skin) 0%, var(--skin) 45%, var(--tunic) 70%, var(--skin) 100%);
  }
  .title-art {
    position: absolute;
    left: 0;
    top: 0;
    width: 802px;
    height: 1200px;
  }
  .title-word {
    font-family: "Archivo Black", "Arial Black", sans-serif;
    fill: var(--title-ink);
  }
  .subtitle {
    position: absolute;
    left: 80px;
    right: 40px;
    top: 835px;
    margin: 0;
    text-align: center;
    font-family: "Open Sans", Arial, sans-serif;
    font-weight: 800;
    font-size: 37px;
    line-height: 47px;
    color: var(--subtitle-red);
  }
  .author {
    position: absolute;
    left: 73px;
    width: 689px;
    top: 1040px;
    margin: 0;
    text-align: center;
    font-family: "Open Sans", Arial, sans-serif;
    font-weight: 800;
    font-size: 62px;
    line-height: 74px;
    color: var(--author-green);
  }
</style>
</head>
<body>
  <main class="cover">
    <div class="cover-frame"></div>

    <div class="hero-illustration" role="img" aria-label="Cartoon strongman in a caveman tunic holding a club, standing on the title words"></div>

    <svg class="title-art" viewBox="0 0 802 1200" aria-labelledby="book-title">
      <title id="book-title">Quieting Gnats, Shouldn'ts and Maybes.</title>
      <text class="title-word" x="94" y="200" font-size="86" textLength="640" lengthAdjust="spacingAndGlyphs">QUIETING</text>
      <text class="title-word" x="200" y="628" font-size="118" textLength="495" lengthAdjust="spacingAndGlyphs">GNATS,</text>
      <text class="title-word" x="132" y="718" font-size="100" textLength="548" lengthAdjust="spacingAndGlyphs">SHOULDN'TS</text>
      <text class="title-word" x="114" y="814" font-size="90" textLength="608" lengthAdjust="spacingAndGlyphs">AND MAYBES.</text>
    </svg>

    <p class="subtitle">Climbing out of<br>the valley of sorrow</p>

    <p class="author">Peter Walsby</p>
  </main>
</body>
</html>
```